Label Design for honey from a small farm in Italy

We need a label for our Acacia's honey .
We are a little farm in Italy and we would like something like organic, raw and simple.
Maybe with botanical drawing with different color like watercolor o something like that (very important natural and easy)
the jar for 1kg of honey: Capacity: 780 ml - Height: 137 mm - Diameter: ∅ 94 mm
- size approx h 5,5 x 10/14cm ( we use the same label for kg and 500 gr jar)

Industry/Entity Type

Farm

Requirements
Must have
• the writings:
- Acacia
- Miele italiano di Acacia
- Da consumarsi preferibilmente entro: ( and below the space to put the date by the hands)
- some space to put some presentation of the farm or some phrases
- our logo
- the space to put the weight by the hands
- Prodotto da Azienda Agricola ...(produced by Farm Name and address....)
- Confezionato presso Apicoltura... (packaged at apiculture Name and address..)
- graphic of Acacia’s flowers ( like drawing)
Should not have
• Barcode
nutritional table

```html
<!DOCTYPE html>
<html lang="it">
<head>
<meta charset="utf-8">
<title>Miele di Acacia – Etichetta</title>
<link rel="stylesheet" href="https://fonts.googleapis.com/css2?family=Oswald:wght@300;400;500&display=swap">
<style>
  :root {
    --canvas: #ebebeb;
    --honey: #f2b418;
    --honey-deep: #e39a0c;
    --panel: #1f2020;
    --mint: #8fc3b4;
    --mint-band: #a6d2c5;
    --text-soft: #b9c9c3;
    --petal: #e9748f;
    --bloom: #f0a020;
    --leaf: #b9d28c;
    --leaf-deep: #9dbb6f;
  }
  * { margin: 0; padding: 0; box-sizing: border-box; }
  html, body {
    width: 1200px; height: 1000px; overflow: hidden;
    background: var(--canvas);
    font-family: "Oswald", sans-serif;
  }
  .label {
    position: absolute; left: 220px; top: 36px;
    width: 760px; height: 928px;
  }
  .honeycomb {
    position: absolute; inset: 0;
    background: linear-gradient(135deg, var(--honey) 0%, var(--honey-deep) 50%, var(--honey) 100%);
  }
  .panel {
    position: absolute; left: 44px; top: 52px;
    width: 680px; height: 690px;
    background: var(--panel);
    clip-path: polygon(0 6%, 6% 0, 94% 0, 100% 6%, 100% 100%, 0 100%);
  }
  .band {
    position: absolute; left: 44px; top: 742px;
    width: 680px; height: 124px;
    background: var(--mint-band);
  }
  .title {
    position: absolute; left: 0; width: 100%; top: 150px;
    text-align: center; color: var(--mint);
    font-size: 80px; font-weight: 400; letter-spacing: 8px; line-height: 1;
  }
  .subtitle {
    position: absolute; left: 0; width: 100%; top: 250px;
    text-align: center; color: var(--mint);
    font-size: 19px; font-weight: 400; letter-spacing: 5px; line-height: 1;
  }
  .best-before {
    position: absolute; left: 0; width: 100%; top: 298px;
    text-align: center; color: var(--text-soft);
    font-size: 15px; font-weight: 300; letter-spacing: 1.5px; line-height: 1;
  }
  .brand {
    position: absolute; left: 0; width: 100%; top: 480px;
    text-align: center; color: var(--mint);
    font-size: 48px; font-weight: 500; letter-spacing: 2px; line-height: 1;
  }
  .producer, .packer {
    position: absolute; top: 628px;
    color: var(--text-soft);
    font-size: 15px; font-weight: 500; letter-spacing: 1px; line-height: 1;
  }
  .producer { left: 100px; }
  .packer { right: 100px; }
  .botanical {
    position: absolute; border-radius: 14px;
  }
  .blossom { background: linear-gradient(160deg, var(--petal), var(--bloom)); }
  .foliage { background: linear-gradient(160deg, var(--leaf), var(--leaf-deep)); }
  .bloom-tl { left: 84px;  top: 142px; width: 110px; height: 110px; }
  .bloom-tr { right: 84px; top: 142px; width: 110px; height: 110px; }
  .leaves-l { left: 64px;  top: 292px; width: 104px; height: 138px; }
  .leaves-r { right: 64px; top: 292px; width: 96px;  height: 138px; }
  .bloom-bl { left: 64px;  top: 452px; width: 76px;  height: 126px; }
  .bloom-br { right: 82px; top: 452px; width: 68px;  height: 136px; }
</style>
</head>
<body>
  <main class="label">
    <div class="honeycomb" role="img" aria-label="Honeycomb pattern in golden yellow and amber"></div>
    <section class="panel"></section>
    <div class="band"></div>

    <div class="botanical blossom bloom-tl" role="img" aria-label="Acacia flower sprig in pink and orange"></div>
    <div class="botanical blossom bloom-tr" role="img" aria-label="Acacia flower sprig in pink and orange"></div>
    <div class="botanical foliage leaves-l" role="img" aria-label="Light green acacia leaves"></div>
    <div class="botanical foliage leaves-r" role="img" aria-label="Light green acacia leaves"></div>
    <div class="botanical blossom bloom-bl" role="img" aria-label="Small acacia blossoms"></div>
    <div class="botanical blossom bloom-br" role="img" aria-label="Small acacia blossoms on a stem"></div>

    <h1 class="title">ACACIA</h1>
    <p class="subtitle">MIELE ITALIANO DI ACACIA</p>
    <p class="best-before">DA CONSUMARSI PREFERIBILMENTE ENTRO:</p>
    <p class="brand">IL POGGIO</p>
    <p class="producer">PRODOTTO DA AZIENDA AGRICOLA</p>
    <p class="packer">CONFEZIONATO PRESSO APICOLTURA</p>
  </main>
</body>
</html>
```